Family Reunion Committee Letterhead

We need a letterhead design for corresponding to families regarding reunion information. And also use the letterhead to send out to potential sponsors and other organizations.

Font styles to use
Serif

Requirements
Must have
• The logo is a must. It should include the following: complete mailing address and email address. The address is P.O. Box 47, Alder Crossing, VT 05640; email address: reunion.desk@mailbrook.net
Nice to have
• N/a
Should not have
• N/a

```html
<!DOCTYPE html>
<html lang="en">
<head>
<meta charset="utf-8">
<title>Tate-Kendall Family Reunion Letterhead</title>
<link rel="stylesheet" href="https://fonts.googleapis.com/css2?family=Crimson+Text:wght@400;600&display=swap">
<style>
  :root {
    --paper: #ffffff;
    --olive: #66683a;
    --footer-text: #f4f2e6;
  }
  html, body {
    margin: 0;
    padding: 0;
    width: 849px;
    height: 1200px;
    overflow: hidden;
    background: var(--paper);
  }
  .letterhead {
    position: relative;
    width: 849px;
    height: 1200px;
    background: var(--paper);
    font-family: "Crimson Text", Georgia, serif;
    overflow: hidden;
  }
  .masthead {
    position: absolute;
    top: 132px;
    left: 0;
    width: 100%;
    display: flex;
    justify-content: center;
    align-items: center;
    gap: 10px;
  }
  .masthead-dot {
    width: 16px;
    height: 16px;
    border-radius: 50%;
    background: var(--olive);
  }
  .masthead-name {
    font-size: 38px;
    font-weight: 600;
    color: var(--olive);
    line-height: 1;
    white-space: nowrap;
  }
  .contact-band {
    position: absolute;
    left: 0;
    bottom: 0;
    width: 100%;
    height: 48px;
    background: var(--olive);
    display: flex;
    justify-content: center;
    align-items: center;
    gap: 14px;
    color: var(--footer-text);
    font-size: 15px;
    white-space: nowrap;
  }
  .contact-divider {
    width: 1px;
    height: 16px;
    background: var(--footer-text);
  }
</style>
</head>
<body>
  <div class="letterhead">
    <header class="masthead">
      <span class="masthead-dot"></span>
      <span class="masthead-name">Tate-Kendall</span>
    </header>

    <footer class="contact-band">
      <span class="contact-address">P.O. Box 47, Alder Crossing, VT 05640</span>
      <span class="contact-divider"></span>
      <span class="contact-email">email address: reunion.desk@mailbrook.net</span>
    </footer>
  </div>
</body>
</html>
```